Business Card Design Project

Hello! We need a business card design for a new company opening up in Downtown Dallas called Marbrook Cupcakes. We are a cupcake factory and our primary colors are Harbor Teal and Brown. We want to have a design that can be used for multiple positions (Owner/Operations Manager, Assistant Operations Manager, Decorator, Baker, Corporate Sale Rep, Special Events Rep etc) We would like for it to be double sided. Use the following information in your designs:

Renata Vasquill
Assistant Operations Manager
renata@marbrookcupcakes.example
T555.318.9047

Store Hours:
Mon-Thur 10am-9pm
Fri-Sat 10am-10pm
Sun 12pm-7pm

website: www.marbrookcupcakes.example

Address: 2735 Quarry Ln, Dallas TX 75999

The logo is attached.

Industry/Entity Type

Business

Requirements
Must have
• It must be Harbor Teal and Brown.
Nice to have
• Nice for it to be double sided.
Should not have
• No graphics like a cupcake. Just the word logo.

```html
<!DOCTYPE html>
<html lang="en">
<head>
<meta charset="utf-8">
<title>Marbrook Cupcakes – Business Card</title>
<link href="https://fonts.googleapis.com/css2?family=Lora:wght@400;700&display=swap" rel="stylesheet">
<style>
  :root {
    --harbor-teal: #5db7be;
    --teal-pale: #e4f2f3;
    --card-white: #f7fbfb;
    --cocoa: #3a2a22;
    --stage: #ecebe8;
    --card-shadow: rgba(40, 30, 20, 0.18);
  }
  * { margin: 0; padding: 0; box-sizing: border-box; }
  html, body {
    width: 1200px;
    height: 901px;
    overflow: hidden;
    background: var(--stage);
    font-family: "Lora", Georgia, serif;
  }
  .card-stage {
    width: 1200px;
    height: 901px;
    display: flex;
    flex-direction: column;
    align-items: center;
    justify-content: center;
    gap: 44px;
  }
  .card {
    position: relative;
    width: 700px;
    height: 400px;
    overflow: hidden;
    box-shadow: 0 8px 24px var(--card-shadow);
  }

  /* Back side: contact details */
  .card--back {
    background: linear-gradient(120deg, var(--card-white) 0%, var(--teal-pale) 100%);
    color: var(--cocoa);
    padding: 44px 0 0 52px;
  }
  .card__name {
    font-size: 34px;
    font-weight: 400;
    line-height: 1;
  }
  .card__title {
    margin-top: 6px;
    font-size: 14px;
    color: var(--harbor-teal);
  }
  .contact-list {
    list-style: none;
    margin-top: 22px;
    font-size: 18px;
    line-height: 1.25;
  }
  .contact-list__label {
    display: inline-block;
    width: 52px;
    color: var(--harbor-teal);
  }
  .store-hours {
    margin: 22px 0 0 28px;
    font-size: 20px;
    line-height: 1.25;
  }
  .store-hours__heading { font-weight: 700; }
  .store-hours__line { color: var(--harbor-teal); font-weight: 700; }
  .card__address {
    margin: 22px 0 0 38px;
    font-size: 18px;
  }

  /* Front side: wordmark */
  .card--front {
    display: flex;
    align-items: center;
    justify-content: center;
  }
  .card__rays {
    position: absolute;
    inset: 0;
    background: radial-gradient(ellipse at 50% 50%, #ffffff 0%, var(--teal-pale) 70%, #d6ecee 100%);
  }
  .wordmark {
    position: relative;
    font-size: 52px;
    font-weight: 400;
    color: var(--harbor-teal);
    letter-spacing: 0.5px;
  }
</style>
</head>
<body>
  <main class="card-stage">
    <section class="card card--back" aria-label="Card back with contact details">
      <h1 class="card__name">Renata Vasquill</h1>
      <p class="card__title">Assistant Operations Manager</p>
      <ul class="contact-list">
        <li><span class="contact-list__label">T:</span>555.318.9047</li>
        <li><span class="contact-list__label">E:</span>renata@marbrookcupcakes.example</li>
        <li><span class="contact-list__label">W:</span>www.marbrookcupcakes.example</li>
      </ul>
      <div class="store-hours">
        <p class="store-hours__heading">Store Hours:</p>
        <p class="store-hours__line">Mon-Thur 10am-9pm</p>
        <p class="store-hours__line">Fri-Sat 10am-10pm</p>
        <p class="store-hours__line">Sun 12pm-7pm</p>
      </div>
      <p class="card__address">Address: 2735 Quarry Ln, Dallas TX 75999</p>
    </section>

    <section class="card card--front" aria-label="Card front with company name">
      <div class="card__rays" role="img" aria-label="Soft pale teal sunburst background pattern"></div>
      <p class="wordmark">Marbrook Cupcakes</p>
    </section>
  </main>
</body>
</html>
```